VoltaRush Product Logo and Package

***Update*** Please you the text from the attached images on the product design.
Suggested Text:
Logo - VoltaRush
Title - Beta-hydroxybutyrates (BHB)Â Ketone Supplement
Beta-hydroxybutyrates (BHB)Â Ketone Supplement
Beta-hydroxybutyrates (BHB)Â Exogenous Ketones
Beta-hydroxybutyrates (BHB)Â Salts
Instant Ketones
3) Flavor - Orange Mango
4) Servings - 30 Servings 12g BHB Per Serving
5) Seals - Made in USA, FDA Certified Facility, GF (gluten Free), Dairy Free, Keto Friendly, Vegan Friendly, Non-GMO, Naturally Flavored, No Preservatives
6) Uses - Energy, Mental Clarity, Fat Loss, Muscle Strength, Appetite Suppression, Mood Management
7) Big Benefit - Formulated To Induce Rapid Ketosis.
Enjoy the benefits of Ketosis anytime!
50% More Servings Compared To Other Leading Brands!
I would like a logo and package designed for a supplement.
It is a powdered supplement that can be packaged in a plastic jar (8-16 oz) or a bag.
We will also be adding additional products to this line and would like the branding to scale.
The product is packaged in a 16 oz tub.
Product Title: Beta-hydroxybutyrates (BHB) Ketone Supplement
Brand Name: VoltaRush (I'd like the logo image to share the E)
Updates
Project Deadline Extended
Reason: I'd like to attract more designers and give them more time to submit briefs.
Target Market(s)
Health and Fitness Enthusiasts. Specifically those interested in a Ketogenic Lifestyle.
Industry/Entity Type
Health And Wellness
Requirements
Must have
- Modern, trendy, design.
- Bold colors and fonts.
- Professional but trendy.
- I would like to see Red and Black as the colors used.
Should not have
- Standard, corporate feel.
- Must be fun, engaging, and exciting.

```html
<!DOCTYPE html>
<html lang="en">
<head>
<meta charset="utf-8">
<title>VoltaRush BHB Ketone Supplement Label</title>
<link rel="stylesheet" href="https://fonts.googleapis.com/css2?family=Archivo:wght@700;800&family=Montserrat:wght@300;400;700;800&family=Roboto+Condensed:wght@300;400&display=swap">
<style>
  :root {
    --label-black: #1b1b1d;
    --label-black-deep: #121214;
    --silver-light: #f2f2f2;
    --silver-mid: #c9c9cb;
    --brand-red: #e4121a;
    --brand-red-dark: #a70a10;
    --text-grey: #a9a9ad;
    --text-soft: #d6d6d8;
    --accent-orange: #f2561f;
    --white: #ffffff;
    --seal-grey: #6e6e72;
  }
  * { box-sizing: border-box; margin: 0; padding: 0; }
  html, body { width: 1163px; height: 1200px; overflow: hidden; background: var(--label-black); }
  .label {
    position: relative;
    width: 1163px;
    height: 1200px;
    background: linear-gradient(90deg, var(--label-black-deep) 0%, var(--label-black) 45%, #232326 70%, var(--label-black-deep) 100%);
    font-family: "Montserrat", sans-serif;
    overflow: hidden;
  }
  .top-band { position: absolute; left: 0; top: 0; width: 1163px; height: 260px; }
  .quality-badge {
    position: absolute; left: 98px; top: 125px;
    width: 200px; height: 108px;
    background: linear-gradient(180deg, var(--white), #e4e4e6);
    border-radius: 8px;
    padding: 14px 16px;
    font-family: "Montserrat", sans-serif; font-weight: 700;
    color: #555558; line-height: 1;
  }
  .quality-badge .big { display: block; font-size: 42px; color: #8a8a8e; letter-spacing: 1px; }
  .quality-badge .small { display: block; font-size: 30px; margin-top: 4px; letter-spacing: 1px; }
  .brand-name {
    position: absolute; right: 60px; top: 68px;
    font-family: "Montserrat", sans-serif; font-weight: 800;
    font-size: 108px; letter-spacing: -3px;
    color: var(--brand-red-dark);
    line-height: 1;
  }
  .product-title {
    position: absolute; left: 98px; top: 300px;
    font-family: "Archivo", sans-serif; font-weight: 800;
    font-size: 71px; letter-spacing: -3px; line-height: 86px;
    color: var(--text-grey);
  }
  .product-title .red { color: var(--brand-red); }
  .benefit-strip { position: absolute; left: 98px; top: 500px; width: 980px; height: 120px; }
  .benefit-text {
    position: absolute; left: 124px; top: 510px;
    font-family: "Roboto Condensed", sans-serif; font-weight: 400;
    font-size: 34px; color: #3a3a3c;
  }
  .strip-tag {
    position: absolute; right: 108px; top: 568px;
    font-family: "Montserrat", sans-serif; font-weight: 700;
    font-size: 30px; letter-spacing: 1px; color: #2a2a2c;
  }
  .uses-list { position: absolute; left: 98px; top: 680px; list-style: none; }
  .uses-list li {
    display: flex; align-items: center; gap: 16px;
    font-family: "Montserrat", sans-serif; font-weight: 400;
    font-size: 37px; color: var(--text-grey);
    height: 50px;
  }
  .uses-list svg { width: 30px; height: 30px; flex: none; }
  .servings-box, .dose-box {
    position: absolute; left: 98px;
    display: flex; align-items: stretch;
    border: 3px solid #9a9a9e; border-radius: 6px;
    background: var(--white);
    font-family: "Roboto Condensed", sans-serif; font-weight: 300;
    overflow: hidden;
    white-space: nowrap;
  }
  .servings-box { top: 918px; height: 74px; }
  .dose-box { top: 1010px; height: 74px; }
  .servings-box .num { font-size: 58px; color: #222; padding: 0 8px; line-height: 68px; letter-spacing: -2px; }
  .servings-box .word { font-size: 58px; color: var(--white); background: var(--brand-red); padding: 0 10px; line-height: 68px; letter-spacing: -2px; }
  .dose-box .num { font-size: 40px; color: #333; padding: 0 8px; line-height: 68px; letter-spacing: -1px; }
  .dose-box .word { font-size: 38px; color: var(--white); background: var(--brand-red); padding: 0 8px; line-height: 68px; letter-spacing: -1.5px; }
  .facility-seal { position: absolute; left: 450px; top: 1026px; width: 120px; height: 56px; }
  .flavor-tag {
    position: absolute; right: 60px; top: 918px;
    width: 300px; height: 104px;
    background: var(--accent-orange);
    color: var(--white); text-align: center;
    font-family: "Montserrat", sans-serif; font-weight: 800;
    padding-top: 12px; line-height: 1;
  }
  .flavor-tag .line1 { display: block; font-size: 27px; }
  .flavor-tag .line2 { display: block; font-size: 38px; margin-top: 6px; }
  .supplement-tag {
    position: absolute; right: 60px; top: 1040px;
    border: 2px solid #7d7d80; border-radius: 4px;
    padding: 6px 10px;
    font-family: "Montserrat", sans-serif; font-weight: 400;
    font-size: 23px; letter-spacing: 1px; color: var(--text-soft);
  }
  .net-weight {
    position: absolute; right: 60px; top: 1100px;
    font-family: "Montserrat", sans-serif; font-weight: 400;
    font-size: 27px; color: var(--text-soft);
  }
  .base-line { position: absolute; left: 0; top: 1150px; width: 1163px; height: 3px; background: var(--brand-red); }
</style>
</head>
<body>
<main class="label">
  <svg class="top-band" viewBox="0 0 1163 260" aria-hidden="true">
    <defs>
      <linearGradient id="silverFill" x1="0" y1="0" x2="0" y2="1">
        <stop offset="0" stop-color="#ffffff"/>
        <stop offset="0.6" stop-color="#e6e6e8"/>
        <stop offset="1" stop-color="#c4c4c6"/>
      </linearGradient>
    </defs>
    <rect x="0" y="0" width="1163" height="230" fill="url(#silverFill)"/>
    <path d="M0 82 H380 C470 82 520 140 560 175 C600 205 640 212 700 212 H1163 V260 H0 Z" fill="var(--brand-red)"/>
    <path d="M0 94 H370 C460 94 505 152 548 188 C590 222 630 228 700 228 H1163 V260 H0 Z" fill="var(--label-black)"/>
  </svg>

  <div class="quality-badge"><span class="big">HEIGH</span><span class="small">QUALITY</span></div>
  <div class="brand-name">VoltaRush</div>

  <h1 class="product-title">
    <span class="red">BETA-</span>HYDROXYBUTYRATES<br>
    (BHB) <span class="red">KETONE SUPPLEMENT</span>
  </h1>

  <svg class="benefit-strip" viewBox="0 0 980 120" aria-hidden="true">
    <path d="M8 0 H980 V50 H560 C520 50 520 30 480 30 H8 Z" fill="#4a4a4d"/>
    <path d="M8 0 H560 C600 0 600 50 640 50 H980 V0 Z" fill="#3c3c3f"/>
    <path d="M0 10 C0 4 4 0 10 0 H500 C540 0 540 50 580 50 H0 Z" fill="#ededef"/>
    <path d="M0 50 H560 C600 50 610 100 660 100 H0 Z" fill="var(--brand-red)"/>
    <path d="M560 50 H980 V90 C980 96 976 100 970 100 H660 C610 100 600 50 560 50 Z" fill="#e2e2e4"/>
  </svg>
  <p class="benefit-text">Formulated To Induce Rapid Ketosis</p>
  <p class="strip-tag">INSTANT KETONES</p>

  <ul class="uses-list">
    <li><svg viewBox="0 0 30 30"><circle cx="15" cy="15" r="12" fill="none" stroke="#a9a9ad" stroke-width="2.5"/><path d="M17 5 L9 17 H15 L12 25 L21 12 H15 Z" fill="#a9a9ad"/></svg>ENERGY, FAT LOSS</li>
    <li><svg viewBox="0 0 30 30"><circle cx="15" cy="15" r="12" fill="none" stroke="#a9a9ad" stroke-width="2.5"/><path d="M17 5 L9 17 H15 L12 25 L21 12 H15 Z" fill="#a9a9ad"/></svg>MUSCLE STRENGTH, APPETITE SUPPRESSION</li>
    <li><svg viewBox="0 0 30 30"><circle cx="15" cy="15" r="12" fill="none" stroke="#a9a9ad" stroke-width="2.5"/><path d="M17 5 L9 17 H15 L12 25 L21 12 H15 Z" fill="#a9a9ad"/></svg>MENTAL CLARITY, MOOD MANAGEMENT</li>
  </ul>

  <div class="servings-box"><span class="num">30</span><span class="word">SERVINGS</span></div>
  <div class="dose-box"><span class="num">12G BHB</span><span class="word">PER SERVING</span></div>

  <svg class="facility-seal" viewBox="0 0 120 56" role="img" aria-label="Registered facility seal">
    <rect x="0" y="0" width="120" height="56" rx="6" fill="var(--seal-grey)"/>
  </svg>

  <div class="flavor-tag"><span class="line1">ORANGE MANGO</span><span class="line2">FLAVOURED</span></div>
  <div class="supplement-tag">DIATARY SUPPLEMENT</div>
  <div class="net-weight">NET WT. 16 OZ.</div>

  <div class="base-line"></div>
</main>
</body>
</html>
```